Bright Fern Landscape Services LLC
business cards, letterhead, and envelopes.
Bright Fern Landscape Services LLC -
Creative Brief
Simple
Lydia Harcourt
Owner
2187 NW 58th Ave. Ocala, Fl 34475
lharcourt@quillmesh.net
Would like to use my tagline somewhere not necessarily right under the logo.

```html
<!DOCTYPE html>
<html lang="en">
<head>
<meta charset="utf-8">
<title>Bright Fern Landscape Services LLC – Business Cards</title>
<link rel="stylesheet" href="https://fonts.googleapis.com/css2?family=Montserrat:wght@600;800&display=swap">
<style>
  :root {
    --green: #2f9a1e;
    --green-dark: #1f7512;
    --lime: #b8d90f;
    --orange: #f7931e;
    --ink: #222222;
    --black: #1c1c1c;
    --white: #ffffff;
    --edge: #9a9a9a;
  }
  * { margin: 0; padding: 0; box-sizing: border-box; }
  html, body { width: 1200px; height: 1021px; overflow: hidden; background: var(--white); }
  body { position: relative; font-family: "Montserrat", Arial, sans-serif; }

  .card {
    position: absolute; width: 533px; height: 308px;
    border: 1px solid var(--edge); overflow: hidden;
  }
  .card--front { left: 339px; top: 28px; height: 318px; background: var(--white); }
  .card--green { left: 50px; top: 367px; background: linear-gradient(100deg, var(--green) 20%, var(--lime) 100%); }
  .card--orange { left: 611px; top: 367px; background: var(--orange); }
  .card--white { left: 50px; top: 692px; background: var(--white); }
  .card--black { left: 611px; top: 692px; background: var(--black); }

  .swoosh { position: absolute; left: 0; top: 0; width: 533px; height: 110px; }

  .brand { position: absolute; display: flex; align-items: center; gap: 10px; }
  .brand__dot { width: 34px; height: 34px; border-radius: 50%; background: var(--orange); flex: none; }
  .brand__name {
    font-weight: 800; font-size: 24px; line-height: 1.1; text-transform: uppercase;
    color: var(--green); white-space: nowrap;
  }
  .tagline {
    position: absolute; font-weight: 600; font-size: 10.5px; text-transform: uppercase;
    letter-spacing: 0.2px; color: var(--green); white-space: nowrap;
  }

  .card--front .brand { left: 28px; top: 100px; }
  .card--front .brand__name { font-size: 19px; }
  .card--front .tagline { left: 28px; top: 152px; font-size: 9px; }

  .holder { position: absolute; right: 70px; top: 190px; text-align center; text-align: center; }
  .holder__name { color: var(--green); font-size: 23px; font-weight: 600; }
  .holder__role { color: var(--ink); font-size: 12px; margin-top: 2px; }

  .contact { position: absolute; left: 28px; top: 214px; font-size: 13px; line-height: 18px; color: var(--ink); font-style: normal; }
  .contact__label { color: var(--green); }

  .card--cover .brand { left: 50%; top: 118px; transform: translateX(-50%); }
  .card--cover .tagline { left: 0; right: 0; top: 184px; text-align: center; }

  .card--green .brand__name { color: var(--white); }
  .card--green .tagline { color: var(--white); }
  .card--orange .brand__dot { background: var(--green-dark); }
  .card--orange .brand__name { color: var(--green-dark); }
  .card--orange .tagline { color: var(--white); }
</style>
</head>
<body>

  <section class="card card--front">
    <svg class="swoosh" viewBox="0 0 533 110" aria-hidden="true">
      <defs>
        <linearGradient id="swooshFill" x1="0" x2="1" y1="0" y2="0">
          <stop offset="0" stop-color="#2f9a1e"/>
          <stop offset="1" stop-color="#b8d90f"/>
        </linearGradient>
      </defs>
      <path d="M0 0 H533 V40 C420 20 300 95 160 80 C90 72 40 60 0 70 Z" fill="url(#swooshFill)"/>
      <path d="M0 76 C40 66 90 78 160 86 C300 101 420 26 533 46" fill="none" stroke="#f7931e" stroke-width="3"/>
    </svg>
    <div class="brand">
      <span class="brand__dot"></span>
      <span class="brand__name">Bright Fern<br>Landscape Services LLC</span>
    </div>
    <p class="tagline">Growing simple spaces into something special.</p>
    <div class="holder">
      <p class="holder__name">Lydia Harcourt</p>
      <p class="holder__role">Owner</p>
    </div>
    <address class="contact">
      2187 NW 58th Ave.<br>
      Ocala, Fl 34475<br>
      <span class="contact__label">Phone:</span> (407) 418-7302<br>
      <span class="contact__label">Email:</span> lharcourt@quillmesh.net
    </address>
  </section>

  <section class="card card--cover card--green">
    <div class="brand"><span class="brand__dot"></span><span class="brand__name">Bright Fern<br>Landscape Services LLC</span></div>
    <p class="tagline">Growing simple spaces into something special.</p>
  </section>

  <section class="card card--cover card--orange">
    <div class="brand"><span class="brand__dot"></span><span class="brand__name">Bright Fern<br>Landscape Services LLC</span></div>
    <p class="tagline">Growing simple spaces into something special.</p>
  </section>

  <section class="card card--cover card--white">
    <div class="brand"><span class="brand__dot"></span><span class="brand__name">Bright Fern<br>Landscape Services LLC</span></div>
    <p class="tagline">Growing simple spaces into something special.</p>
  </section>

  <section class="card card--cover card--black">
    <div class="brand"><span class="brand__dot"></span><span class="brand__name">Bright Fern<br>Landscape Services LLC</span></div>
    <p class="tagline">Growing simple spaces into something special.</p>
  </section>

</body>
</html>
```